I need an invite for a customer appreciation event for Bramwell Seed. The event will take place on January 3rd, 2025 at Copper Hollow (1836 Ridgeway Lane, Hamburg, IA, United States, Iowa) and begin at 6:00pm. Agenda is 6:00pm cocktail hour, 6:30pm Dinner, 8:00pm Entertainment.
Entertainment is Wade Dunbrook & The Dusty Porch Ramblers.
Diner will be choice of Prime Rib, Chicken Breast or Pork Chop
RSVP Curtis Ollam with meal choice and guest list at 402-555-0193 call or text
Raffle Prize will be Harvestline Neon Logo Sign and a Glacier Cooler
Would like to include the logos and pictures that have been uploaded.
This event is for farmers so cornfields for backgrounds or anything ag related would be good.

```html
<!DOCTYPE html>
<html lang="en">
<head>
<meta charset="utf-8">
<title>Bramwell Seed – Customer Appreciation Event</title>
<link rel="stylesheet" href="https://fonts.googleapis.com/css2?family=Allura&family=Cinzel:wght@400;500;600&display=swap">
<style>
  :root {
    --paper: #ffffff;
    --frame: #1f3b3e;
    --frame-shadow: #c9cfd1;
    --ink: #1d1d1d;
    --leaf: #8ec8ca;
    --leaf-light: #c4e4e4;
    --green: #5aab4f;
    --green-light: #8fcd7e;
    --rule: #8ec8ca;
    --stripe: #cfd3d4;
  }
  * { margin: 0; padding: 0; box-sizing: border-box; }
  html, body { width: 800px; height: 1200px; overflow: hidden; background: var(--paper); }
  .invite {
    position: relative;
    width: 800px;
    height: 1200px;
    overflow: hidden;
    background: var(--paper);
    font-family: "Cinzel", serif;
    color: var(--ink);
  }
  .backdrop { position: absolute; inset: 0; }
  .brand {
    position: absolute;
    top: 110px;
    left: 0;
    width: 800px;
    height: 180px;
    display: flex;
    justify-content: center;
    align-items: center;
    gap: 12px;
  }
  .brand-mark { width: 18px; height: 18px; background: var(--green); }
  .brand-name {
    font-weight: 600;
    font-size: 30px;
    color: var(--frame);
    letter-spacing: 1px;
  }
  h1 { font-weight: 400; }
  .title { position: absolute; left: 0; width: 800px; text-align: center; display: block; }
  .title-script {
    font-family: "Allura", cursive;
    color: var(--green);
    font-size: 124px;
    line-height: 1;
  }
  .title-customer { top: 340px; }
  .title-main {
    top: 468px;
    font-family: "Cinzel", serif;
    font-weight: 500;
    font-size: 52px;
    line-height: 60px;
    letter-spacing: 10px;
    color: var(--ink);
  }
  .title-event { top: 532px; }
  .details {
    position: absolute;
    top: 700px;
    left: 120px;
    width: 560px;
    text-align: center;
    font-size: 18px;
    line-height: 23px;
    color: var(--ink);
  }
  .details p + p { margin-top: 10px; }
  .details .extra { font-size: 16px; line-height: 21px; }
  .contact {
    position: absolute;
    top: 988px;
    left: 0;
    width: 800px;
    display: flex;
    justify-content: center;
    align-items: center;
    gap: 8px;
    font-size: 21px;
    color: var(--ink);
  }
  .contact svg { width: 14px; height: 22px; }
</style>
</head>
<body>
<main class="invite">
  <svg class="backdrop" width="800" height="1200" viewBox="0 0 800 1200">
    <defs>
      <linearGradient id="leafTone" x1="0" y1="0" x2="1" y2="1">
        <stop offset="0" stop-color="var(--leaf-light)"/>
        <stop offset="1" stop-color="var(--leaf)"/>
      </linearGradient>
      <linearGradient id="fieldTone" x1="0" y1="0" x2="0" y2="1">
        <stop offset="0" stop-color="var(--green-light)"/>
        <stop offset="1" stop-color="var(--green)"/>
      </linearGradient>
    </defs>

    <g role="img" aria-label="Rolling cornfield band along the bottom of the invitation">
      <path d="M40 1130 C120 1080 250 1040 420 1052 C560 1062 700 1060 800 1040 L800 1200 L40 1200 Z" fill="var(--green-light)"/>
      <path d="M55 1150 C150 1095 270 1055 420 1062 C560 1070 700 1068 800 1052 L800 1200 L55 1200 Z" fill="url(#fieldTone)"/>
    </g>

    <rect class="frame-shadow" x="74" y="72" width="666" height="1074" fill="none" stroke="var(--frame-shadow)" stroke-width="6"/>
    <rect class="frame" x="64" y="62" width="670" height="1078" fill="none" stroke="var(--frame)" stroke-width="9"/>

    <circle class="accent-circle" cx="140" cy="1053" r="53" fill="var(--stripe)" role="img" aria-label="Striped decorative circle"/>

    <g role="img" aria-label="Teal fern leaf illustration, top right">
      <ellipse cx="700" cy="310" rx="60" ry="210" transform="rotate(-28 700 310)" fill="url(#leafTone)"/>
    </g>
    <g role="img" aria-label="Teal fern leaf illustration, bottom left">
      <ellipse cx="90" cy="890" rx="55" ry="175" transform="rotate(35 90 890)" fill="url(#leafTone)"/>
    </g>

    <line class="divider" x1="127" y1="672" x2="673" y2="672" stroke="var(--rule)" stroke-width="2"/>
  </svg>

  <div class="brand">
    <span class="brand-mark"></span>
    <span class="brand-name">Bramwell Seed</span>
  </div>

  <h1>
    <span class="title title-script title-customer">Customer</span>
    <span class="title title-main">Appreciation</span>
    <span class="title title-script title-event">Event</span>
  </h1>

  <section class="details">
    <p>event on January 3rd, 2025 at Copper Hollow (1836 Ridgeway Lane, Hamburg, IA, United States, Iowa) and begin at 6:00pm. Agenda is 6:00pm cocktail hour, 6:30pm Dinner, 8:00pm Entertainment</p>
    <p>Entertainment for Wade Dunbrook &amp; The Dusty Porch Ramblers</p>
    <p class="extra">Dinner: choice of Prime Rib, Chicken Breast or Pork Chop</p>
    <p class="extra">Raffle: Harvestline Neon Logo Sign &amp; a Glacier Cooler</p>
    <p class="extra">RSVP Curtis Ollam with meal choice &amp; guest list, call or text</p>
  </section>

  <div class="contact">
    <svg viewBox="0 0 14 22" aria-hidden="true"><rect x="1" y="1" width="12" height="20" rx="2" fill="var(--green)"/><rect x="5" y="17" width="4" height="1.6" rx="0.8" fill="#ffffff"/></svg>
    <span>402-555-0193</span>
  </div>
</main>
</body>
</html>
```